Website Design for new skincare product launch/rebranding

The Dew Meridian website is currently live and built through Pagevolt.com. While the existing site has served as a strong starting point, I’m now looking to elevate the overall experience with a complete redesign that reflects the growth and vision of the brand. This will be a full visual and functional revamp — not just a refresh — with the goal of creating a more elevated, intuitive, and conversion-focused platform. I’m looking for a designer who can not only reimagine the layout and visuals, but also collaborate on optimizing the user journey and site structure for both storytelling and sales.

Target Market(s)

Age 25- 45 (core), with secondary appeal to 18-55. Primarily women, but gender inclusive. Wellness/Holistic Beauty/Organic Ingredients, Botanical.

Industry/Entity Type

Beauty, aesthetics, wellness.

Number of Pages Required

5+ page

Font styles to use
Other font styles liked:
• Gravesned Sans Family

Colors

Designer to choose colors to be used in the design.

Requirements
Must have
• Include standard pages (Home, Our Story/Values, Shop, Product Detail with ingredients/description/etc., Contact) and any other recommended sections to optimize conversion. Minimal, clean, calming visual. Seamlessly integrate with Cartwell for all product sales.
Nice to have
• Company colors are attached in images, along with first two products that are launching. One called Velunmist, and one called Petravelle. Fonts and shapes need to align accordingly. Feel elevated, neutral, and luxe while maintaining a grounded, earthy minimalism. Visual inspiration includes brands like Lantern Grove, Marble Osprey, and TOvelin — minimal yet high-end, with thoughtful use of whitespace, typography, and subtle movement. Would LOVE to have movement (short clip GIF) on either the home page or ingredient page, reference TOvelin website (homepage or LuminWeave System™ Tab)
Should not have
• dark colors, complex design elements, too many different fonts. For ingredients, stick to botanical images and information only, with no mentions of CBD or use of leaf imagery.

```html
<!DOCTYPE html>
<html lang="en">
<head>
<meta charset="utf-8">
<title>Dew Meridian — Where Skin Meets Balance</title>
<link rel="stylesheet" href="https://fonts.googleapis.com/css2?family=Montserrat:wght@400;500;600;700;800&family=Jost:wght@300;400;500;600&display=swap">
<style>
:root{
  --page:#f5f5f4;
  --white:#ffffff;
  --band:#ededec;
  --ink:#1c1c1c;
  --muted:#6c6b68;
  --soft:#bdbcb8;
  --sand:#dcd2c9;
  --sand-deep:#c9bcb0;
  --oil:#d8c15a;
  --footer:#9d9c96;
  --line:#e2e1de;
}
*{box-sizing:border-box;margin:0;padding:0}
html,body{width:1200px;height:4112px;overflow:hidden}
body{background:var(--page);font-family:"Jost",sans-serif;color:var(--ink);position:relative}
.abs{position:absolute}
h1,h2,h3,h4{font-family:"Montserrat",sans-serif;font-weight:800;text-transform:uppercase;letter-spacing:.02em}
p{font-size:12px;line-height:1.6;color:var(--muted)}

/* nav */
.nav{top:0;left:0;width:1200px;height:60px}
.brand{left:72px;top:10px;text-align:center}
.brand .mark{display:block;width:22px;height:22px;border:1.5px solid var(--ink);border-radius:50%;margin:0 auto 3px}
.brand .name{font-family:"Montserrat",sans-serif;font-weight:600;font-size:12px;letter-spacing:.14em;text-transform:uppercase}
.nav-links{right:290px;top:22px;display:flex;gap:28px;font-family:"Montserrat",sans-serif;font-size:10px;font-weight:600;letter-spacing:.06em}
.nav-icons{right:200px;top:20px;display:flex;gap:14px}
.btn{display:inline-block;background:var(--sand);border-radius:20px;font-family:"Montserrat",sans-serif;font-weight:700;font-size:10px;letter-spacing:.06em;text-transform:uppercase;padding:9px 22px;color:var(--ink)}
.nav .btn{position:absolute;right:72px;top:14px}

/* hero */
.hero{top:0;left:0;width:1200px;height:760px;background:var(--page)}
.hero-title{left:72px;top:218px;font-size:76px;line-height:.98;letter-spacing:.01em}
.hero-title .outline{color:transparent;-webkit-text-stroke:1.5px var(--soft)}
.hero-sub{left:72px;top:452px;width:300px}
.hero .btn{position:absolute;left:72px;top:536px}
.scroll-cue{left:72px;top:650px;width:38px;height:56px;border:1.5px solid var(--soft);border-radius:20px}
.hero-visual{left:520px;top:96px;width:420px;height:620px;border-radius:8px;background:linear-gradient(180deg,#f3f3f2 0%,#e6e5e3 55%,#cfc9bf 100%)}
.vertical-word{font-family:"Montserrat",sans-serif;font-weight:800;text-transform:uppercase;color:#e3e2df;writing-mode:vertical-rl;letter-spacing:.06em}
.hero .vertical-word{right:30px;top:90px;font-size:58px}

/* values */
.values-title{top:806px;left:0;width:1200px;text-align:center;font-size:30px;line-height:1.25}
.values{top:950px;left:150px;width:900px;display:flex;justify-content:space-between}
.value{width:260px;text-align:center}
.value .icon{width:70px;height:70px;border-radius:50%;background:var(--band);margin:0 auto 22px;display:flex;align-items:center;justify-content:center}
.value h4{font-size:12px;margin-bottom:8px}

/* collection */
.collection-head{top:1216px;left:150px;width:900px;height:110px;background:var(--white);border-radius:12px;box-shadow:0 6px 18px rgba(0,0,0,.05)}
.collection-head h2{position:absolute;left:40px;top:22px;font-size:30px;line-height:1.15}
.collection-head p{position:absolute;left:450px;top:18px;width:420px;font-size:11px}
.product{background:var(--white);box-shadow:0 6px 22px rgba(0,0,0,.06)}
.product .shot{position:absolute;left:0;top:0;width:100%;border-radius:2px;background:linear-gradient(180deg,#fbfbfb 0%,#f4f3f1 62%,var(--sand) 62%,var(--sand) 100%)}
.product h3{position:absolute;left:12px;font-size:13px}
.product p{position:absolute;left:12px;width:340px;font-size:10.5px;line-height:1.5}
.product .link{position:absolute;left:12px;font-family:"Montserrat",sans-serif;font-weight:700;font-size:9.5px;letter-spacing:.04em}
.p1{left:176px;top:1380px;width:384px;height:480px}
.p2{left:614px;top:1460px;width:384px;height:580px}

/* about */
.about{top:2090px;left:0;width:1200px;height:1140px;background:var(--band)}
.about .vertical-word{left:40px;top:400px;font-size:70px;color:#dedddb;transform:rotate(180deg)}
.about-head{left:150px;top:90px;width:900px;height:130px;background:var(--white);border-radius:12px;box-shadow:0 6px 18px rgba(0,0,0,.05)}
.about-head h2{position:absolute;left:40px;top:28px;font-size:27px;line-height:1.15}
.about-head p{position:absolute;left:470px;top:24px;width:400px;font-size:11px}
.story-card{background:var(--white);border-radius:14px;box-shadow:0 6px 18px rgba(0,0,0,.05)}
.story-card .num{position:absolute;left:28px;top:28px;width:38px;height:38px;border-radius:50%;border:1.5px solid var(--ink);font-family:"Montserrat",sans-serif;font-weight:700;font-size:15px;display:flex;align-items:center;justify-content:center}
.story-card h3{position:absolute;left:28px;top:84px;font-size:17px}
.story-card p{position:absolute;left:28px;top:118px;width:360px;font-size:11px}
.c1{left:168px;top:280px;width:432px;height:290px}
.c2{left:616px;top:780px;width:410px;height:270px}
.photo{border-radius:14px}
.ph1{left:620px;top:270px;width:404px;height:360px;background:linear-gradient(160deg,#e9e4dc 0%,#c7b08e 55%,#8e7a55 100%)}
.ph2{left:176px;top:588px;width:406px;height:400px;background:linear-gradient(180deg,#7f9a70 0%,#6d8b66 40%,#3f6a76 100%)}

/* testimonials */
.testimonials-title{top:3312px;left:0;width:1200px;text-align:center;font-size:28px}
.review{left:240px;top:3380px;width:720px;height:188px;background:var(--white);border-radius:8px;box-shadow:0 8px 24px rgba(0,0,0,.07)}
.review .avatar{position:absolute;left:22px;top:20px;width:96px;height:146px;border-radius:48px;background:linear-gradient(180deg,#cdb6a0 0%,#8a6b55 100%)}
.review .stars{position:absolute;left:140px;top:26px;display:flex;gap:3px}
.review p{position:absolute;left:140px;top:46px;width:450px;font-size:11px}
.review .who{position:absolute;left:140px;top:146px;font-family:"Montserrat",sans-serif;font-weight:700;font-size:11px;letter-spacing:.04em}
.review .quote{position:absolute;right:24px;bottom:22px;font-family:"Montserrat",sans-serif;font-size:48px;color:var(--soft);line-height:1}
.dots{top:3618px;left:576px;display:flex;gap:6px}
.dots span{width:8px;height:3px;border-radius:2px;background:var(--soft)}
.dots span.on{background:var(--ink);width:14px}

/* newsletter */
.newsletter h2{position:absolute;left:72px;top:3696px;font-size:26px}
.newsletter p{position:absolute;left:72px;top:3732px;font-size:11px}
.signup{left:644px;top:3706px;width:488px;height:34px;display:flex;align-items:center}
.signup .field{flex:1;height:34px;background:var(--white);border-radius:4px 0 0 4px;font-size:10px;color:var(--soft);padding:10px 14px}
.signup .btn{border-radius:18px;margin-left:-10px;padding:10px 24px}

/* footer */
.footer{left:0;top:3866px;width:1200px;height:246px;background:var(--footer);color:var(--white)}
.footer .brand{left:72px;top:40px}
.footer .brand .mark{border-color:var(--white);width:30px;height:30px}
.footer .brand .name{font-size:17px;color:var(--white)}
.footer .links{position:absolute;right:72px;top:124px;display:flex;gap:30px;font-family:"Montserrat",sans-serif;font-size:10px;font-weight:600;letter-spacing:.06em}
.footer .rule{position:absolute;left:72px;top:172px;width:1056px;height:1px;background:rgba(255,255,255,.35)}
.footer .copy{position:absolute;left:72px;top:196px;font-size:10px;letter-spacing:.06em;text-transform:uppercase}
.footer .social{position:absolute;right:72px;top:188px;display:flex;gap:10px}
.footer .social span{width:26px;height:26px;border-radius:50%;background:rgba(255,255,255,.25)}
</style>
</head>
<body>

<section class="hero abs">
  <div class="hero-visual abs" role="img" aria-label="Two frosted serum bottles with golden oil and droppers resting on a round stone plinth"></div>
  <span class="vertical-word abs">Dew Meridian</span>
  <h1 class="hero-title abs">Where<br>Skin <span class="outline">Meets</span><br>Balance</h1>
  <p class="hero-sub abs">Botanical beauty rituals, mindfully formulated to nourish, protect, and align your skin.</p>
  <a class="btn">Shop the collection</a>
  <div class="scroll-cue abs">
    <svg width="38" height="56" viewBox="0 0 38 56"><path d="M19 20v14M14 29l5 5 5-5" fill="none" stroke="#1c1c1c" stroke-width="1.4"/></svg>
  </div>
</section>

<header class="nav abs">
  <div class="brand abs"><span class="mark"></span><span class="name">Dew Meridian</span></div>
  <nav class="nav-links abs"><span>HOME</span><span>OUR STORY</span><span>SHOP</span><span>PRODUCT DETAIL</span></nav>
  <div class="nav-icons abs">
    <svg width="14" height="14" viewBox="0 0 14 14"><circle cx="6" cy="6" r="4.5" fill="none" stroke="#1c1c1c" stroke-width="1.3"/><path d="M9.5 9.5L13 13" stroke="#1c1c1c" stroke-width="1.3"/></svg>
    <svg width="14" height="14" viewBox="0 0 14 14"><circle cx="7" cy="4.5" r="3" fill="none" stroke="#1c1c1c" stroke-width="1.3"/><path d="M1.5 13.5c1-3 3-4.5 5.5-4.5s4.5 1.5 5.5 4.5" fill="none" stroke="#1c1c1c" stroke-width="1.3"/></svg>
    <svg width="14" height="14" viewBox="0 0 14 14"><path d="M1 1.5h2l1.6 8h7l1.4-6H4" fill="none" stroke="#1c1c1c" stroke-width="1.3"/><circle cx="5.5" cy="12.3" r="1" fill="#1c1c1c"/><circle cx="11" cy="12.3" r="1" fill="#1c1c1c"/></svg>
  </div>
  <a class="btn">Contact</a>
</header>

<h2 class="values-title abs">Grounded in nature, backed<br>by science</h2>
<div class="values abs">
  <div class="value">
    <div class="icon"><svg width="30" height="30" viewBox="0 0 30 30"><circle cx="15" cy="15" r="11" fill="none" stroke="#1c1c1c" stroke-width="1.3"/><circle cx="15" cy="15" r="4" fill="none" stroke="#1c1c1c" stroke-width="1.3"/></svg></div>
    <h4>Botanical ingredients</h4>
    <p>We source high-quality plant-powered ingredients that are gentle, effective and rooted in nature.</p>
  </div>
  <div class="value">
    <div class="icon"><svg width="30" height="30" viewBox="0 0 30 30"><rect x="10" y="4" width="10" height="22" rx="3" fill="none" stroke="#1c1c1c" stroke-width="1.3"/><path d="M10 12h10" stroke="#1c1c1c" stroke-width="1.3"/></svg></div>
    <h4>Holistic formulations</h4>
    <p>Each product is thoughtfully designed to support skin health from every angle of balance.</p>
  </div>
  <div class="value">
    <div class="icon"><svg width="30" height="30" viewBox="0 0 30 30"><path d="M22 8a10 10 0 1 0 2 9" fill="none" stroke="#1c1c1c" stroke-width="1.3"/><path d="M18 8h4V4" fill="none" stroke="#1c1c1c" stroke-width="1.3"/></svg></div>
    <h4>Sustainable practices</h4>
    <p>From packaging to production, we prioritize practices that are kind to the earth and to you.</p>
  </div>
</div>

<div class="collection-head abs">
  <h2>Our debut<br>collection</h2>
  <p>A first glimpse into our philosophy of functional beauty. These two formulations were created to bring hydration, harmony, and ritual into your everyday — using high-performing botanicals and modern skin science.</p>
</div>

<article class="product p1 abs">
  <div class="shot" style="height:330px" role="img" aria-label="Petravelle serum bottle with dropper on a sand-toned base"></div>
  <h3 style="top:346px">Petravelle</h3>
  <p style="top:366px">A daily moisture serum designed to support the skin barrier, balance hydration, and deliver long-lasting radiance — all with a lightweight, plant-based texture.</p>
  <span class="link" style="top:430px">VIEW DETAILS</span>
</article>
<article class="product p2 abs">
  <div class="shot" style="height:420px" role="img" aria-label="Velunmist serum bottle with dropper on a sand-toned base"></div>
  <h3 style="top:440px">Velunmist</h3>
  <p style="top:460px">A lightweight botanical serum that locks in hydration and leaves skin visibly smooth, dewy, and glassy without the weight.</p>
  <span class="link" style="top:510px">VIEW DETAILS</span>
</article>

<section class="about abs">
  <span class="vertical-word abs">About us</span>
  <div class="about-head abs">
    <h2>Elevated<br>skin wellness,<br>naturally</h2>
    <p>At Dew Meridian, we believe that beauty blooms through balance. Our formulations are crafted with purpose — blending potent botanicals with modern skin science to support your skin's rhythm naturally.</p>
  </div>
  <div class="story-card c1 abs">
    <span class="num">1</span>
    <h3>Consciously formulated</h3>
    <p>We're deeply intentional about what goes into every bottle. Each ingredient is chosen not just for what it does but for how it connects to the skin and the planet. No fillers, no harsh synthetics — only purposeful botanicals that work in harmony with your skin's natural ecosystem.</p>
  </div>
  <div class="photo ph1 abs" role="img" aria-label="Woman with curly hair smiling outdoors while holding a serum bottle"></div>
  <div class="photo ph2 abs" role="img" aria-label="Woman in a white dress with a green flower crown sitting in a boat on calm water"></div>
  <div class="story-card c2 abs">
    <span class="num">2</span>
    <h3>Rooted in ritual</h3>
    <p>Skincare shouldn't feel like a chore — it should feel like coming home to yourself. Our products are designed to be more than just effective — they're sensorial, grounding, and made to encourage slow, nourishing moments of self-connection each day.</p>
  </div>
</section>

<h2 class="testimonials-title abs">Testimonials</h2>
<div class="review abs">
  <div class="avatar" role="img" aria-label="Portrait of a customer with long dark hair"></div>
  <div class="stars">
    <svg width="72" height="12" viewBox="0 0 72 12"><g fill="#d9a441"><path id="s" d="M6 0l1.8 3.8 4.2.5-3.1 2.9.8 4.1L6 9.3 2.3 11.3l.8-4.1L0 4.3l4.2-.5z"/><use href="#s" x="15"/><use href="#s" x="30"/><use href="#s" x="45"/><use href="#s" x="60"/></g></svg>
  </div>
  <p>After using the serum for just a week, my skin looks noticeably brighter and more even. It feels like a reset for my face. My skin has always been sensitive, but this one calmed the redness without feeling heavy. It's now my ritual.</p>
  <span class="who">MIRA T SENSITIVE SKIN</span>
  <span class="quote">”</span>
</div>
<div class="dots abs"><span class="on"></span><span></span><span></span></div>

<section class="newsletter">
  <h2>Let's stay aligned</h2>
  <p>Be the first to know about new launches, rituals, and exclusive offers.</p>
  <div class="signup abs"><span class="field">Enter Your Email Address...</span><a class="btn">Subscribe now</a></div>
</section>

<footer class="footer abs">
  <div class="brand abs"><span class="mark"></span><span class="name">Dew Meridian</span></div>
  <nav class="links"><span>HOME</span><span>OUR STORY</span><span>SHOP</span><span>PRODUCT DETAIL</span><span>CONTACT</span></nav>
  <div class="rule"></div>
  <span class="copy">Copyright 2025. All rights reserved.</span>
  <div class="social"><span></span><span></span><span></span><span></span></div>
</footer>

</body>
</html>
```